Premium small-production winery needs a front label redesign

We produce wine from cold-climate varietal grapes, many of which were only developed in the last 50 years. Our winery, called Hollow Ridge Cellars, is housed in an industrial style building serving a premium product. We have 12 styles of wine that can accommodate a wide range of tastes. We would like to see designs that communicate old traditions (winemaking styles) blended with new ideas (newly developed grape varieties). Our ideal customer enjoys an evening that is cultured and classy, yet fun and educational. We will likely favor designs that are 4" x 4.5", but this isn't required - if we see something we love, we would consider changing the dimensions.
I've attached our current labels and 2 logo files. We are only looking for a front-label redesign. Thanks!

Target Market(s)

Our ideal customer enjoys an evening that is cultured and classy, yet fun and educational.

Font styles to use
Serif
Sans Serif
Script
Other font styles liked:
• Our current fonts are Trajan Pro, Tangerine, and Avenir.

Requirements
Must have
• We would love to see a design that could span our entire product line with only a subtle or minor change (such as printing color, or a picture) to distinguish between our 12 products. Emphasis on the part about the change should be subtle among labels.
• Some of the distinguishing characteristics of the wines:
• Color: white, orange, rosé (pink), light red, dark red
• Sweetness: dry, off-dry, semi-sweet, sweet, very sweet
• Flavors: too many to list
• Product names: 9 of the wines are named after the majority grape. The other 3 are blends of multiple grapes, with the following names: "Velvet Blush", "Opal", and "Ember".
Nice to have
• our wine list: http://hollowridgecellars.example/wine/
Should not have
• We would prefer a design that isn't too busy overall.

```html
<!DOCTYPE html>
<html lang="en">
<head>
<meta charset="utf-8">
<title>Hollow Ridge Cellars — Opal Front Label</title>
<link href="https://fonts.googleapis.com/css2?family=Cinzel:wght@400&family=Tangerine:wght@400&display=swap" rel="stylesheet">
<style>
  :root {
    --paper: #ffffff;
    --label-black: #000000;
    --wine: #7b2931;
    --halo: rgba(120, 70, 80, 0.55);
  }
  html, body {
    margin: 0;
    padding: 0;
    width: 1067px;
    height: 1200px;
    overflow: hidden;
    background: var(--paper);
  }
  .label {
    position: relative;
    width: 1067px;
    height: 1200px;
    overflow: hidden;
    background: var(--paper);
  }
  .label__panel {
    position: absolute;
    left: 62px;
    top: 52px;
    width: 960px;
    height: 1104px;
    background: var(--label-black);
    border-radius: 22px;
    box-shadow: 0 0 22px 18px var(--label-black), 0 0 40px 30px var(--halo);
  }
  .label__bands {
    position: absolute;
    left: 0;
    top: 0;
  }
  .brand-mark {
    position: absolute;
    left: 0;
    top: 300px;
    width: 1067px;
    text-align: center;
    font-family: "Cinzel", serif;
    font-size: 44px;
    letter-spacing: 4px;
    color: var(--wine);
    margin: 0;
  }
  .brand-line {
    position: absolute;
    margin: 0;
    font-family: "Cinzel", serif;
    font-weight: 400;
    line-height: 1;
    white-space: nowrap;
  }
  .brand-line--first {
    left: 135px;
    top: 620px;
    font-size: 74px;
    color: var(--paper);
  }
  .brand-line--second {
    left: 137px;
    top: 716px;
    font-size: 74px;
    color: var(--wine);
  }
  .wine-name {
    position: absolute;
    left: 140px;
    top: 790px;
    margin: 0;
    font-family: "Tangerine", cursive;
    font-size: 230px;
    line-height: 1;
    color: var(--wine);
  }
</style>
</head>
<body>
  <main class="label">
    <div class="label__panel"></div>

    <svg class="label__bands" width="1067" height="1200" viewBox="0 0 1067 1200" aria-hidden="true">
      <polygon class="band band--wine" points="0,609 876,609 782,704 0,704" fill="var(--wine)"/>
      <polygon class="band band--light" points="0,704 633,704 538,800 0,800" fill="var(--paper)"/>
    </svg>

    <p class="brand-mark">Hollow Ridge Cellars</p>

    <h1 class="brand-line brand-line--first">Hollow Ridge</h1>
    <p class="brand-line brand-line--second">Cellars</p>

    <h2 class="wine-name">Opal</h2>
  </main>
</body>
</html>
```